Advert for e-news letter

I have a property valuation business and this is an advert for one specific service. The service is for Lot Entitlements and is directed at conveyancers. I have attached a company logo. The sizing of the advert (as noted in Media kit) – will be 158px x 170 px.
Advert to summarise the following;
Do you have developer clients? We can help with Lot Entitlements for Land Division. We believe that our prices are the best in the market, however should you provide a cheaper written quote we will beat it by 15%.
Pricing for RVB compliant Lot Entitlement Certificates.
• 1 Allotment into 2 Community Titled Lots: $220 Inc GST (2 day turnaround)
• 1 Allotment into 3 Community Titled Lots: $275 Inc GST (2 day turnaround)
• 1 Allotment into 4 or 5 Community Titled Lots: $330 Inc GST (2 day turnaround)
• 6 or more or Commercial: By Quote

```html
<!DOCTYPE html>
<html lang="en">
<head>
<meta charset="utf-8">
<title>Halden – Lot Entitlements Advert</title>
<link href="https://fonts.googleapis.com/css2?family=Cabin:wght@700&family=Arimo:wght@400;700&display=swap" rel="stylesheet">
<style>
  :root {
    --frame-blue: #19a6e2;
    --green-top: #13bb9c;
    --green-bottom: #037a60;
    --band-yellow: #ffe400;
    --band-pale: #fffbe6;
    --tick-red: #e8173f;
    --ink: #111111;
    --logo-ink: #2a2a2a;
    --logo-teal: #1fb3a2;
    --white: #ffffff;
  }
  html, body {
    margin: 0;
    padding: 0;
    width: 1188px;
    height: 1200px;
    overflow: hidden;
    background: var(--white);
  }
  .advert {
    position: absolute;
    left: 222px;
    top: 204px;
    width: 658px;
    height: 704px;
    border: 4px solid var(--frame-blue);
    background: var(--white);
    overflow: hidden;
  }
  .advert__backdrop {
    position: absolute;
    inset: 0;
  }
  .brand {
    position: absolute;
    left: 30px;
    top: 30px;
    display: flex;
    align-items: center;
    gap: 14px;
  }
  .brand__mark {
    width: 46px;
    height: 46px;
    background: var(--logo-teal);
  }
  .brand__name {
    font-family: "Cabin", sans-serif;
    font-weight: 700;
    font-size: 40px;
    color: var(--logo-ink);
    letter-spacing: 1px;
  }
  .headline {
    position: absolute;
    left: 26px;
    top: 150px;
    margin: 0;
    font-family: "Cabin", sans-serif;
    font-weight: 700;
    font-size: 43px;
    color: var(--ink);
    white-space: nowrap;
    transform-origin: left bottom;
    transform: rotate(-13deg);
  }
  .pitch {
    position: absolute;
    left: 30px;
    top: 308px;
    width: 360px;
    margin: 0;
    font-family: "Cabin", sans-serif;
    font-weight: 700;
    font-size: 31px;
    line-height: 40px;
    color: var(--white);
  }
  .pitch__figure {
    font-size: 46px;
    line-height: 54px;
  }
  .pricing {
    position: absolute;
    left: 394px;
    top: 202px;
    width: 258px;
    font-family: "Arimo", sans-serif;
    color: var(--white);
  }
  .pricing__title {
    margin: 0 0 4px;
    font-weight: 700;
    font-size: 19px;
    line-height: 25px;
  }
  .pricing__list {
    list-style: none;
    margin: 0;
    padding: 0;
    font-size: 19.5px;
    line-height: 28px;
  }
  .pricing__item {
    position: relative;
    padding-left: 12px;
    margin-bottom: 0;
  }
  .pricing__item::before {
    content: "•";
    position: absolute;
    left: 0;
    font-size: 14px;
  }
  .pricing__item span { display: block; line-height: 26px; }
</style>
</head>
<body>
  <section class="advert">
    <svg class="advert__backdrop" width="658" height="704" viewBox="0 0 658 704" aria-hidden="true">
      <defs>
        <linearGradient id="greenFill" x1="0" y1="0" x2="0" y2="1">
          <stop offset="0" stop-color="var(--green-top)"/>
          <stop offset="1" stop-color="var(--green-bottom)"/>
        </linearGradient>
        <linearGradient id="bandFill" x1="0" y1="0" x2="1" y2="0">
          <stop offset="0" stop-color="var(--band-yellow)"/>
          <stop offset="0.45" stop-color="var(--band-pale)"/>
          <stop offset="0.75" stop-color="var(--band-pale)"/>
          <stop offset="1" stop-color="var(--band-yellow)"/>
        </linearGradient>
        <linearGradient id="bandShade" x1="0" y1="0" x2="0" y2="1">
          <stop offset="0" stop-color="#0b6e5a" stop-opacity="0.55"/>
          <stop offset="1" stop-color="#0b6e5a" stop-opacity="0"/>
        </linearGradient>
      </defs>
      <polygon points="0,252 658,127 658,704 0,704" fill="url(#greenFill)"/>
      <polygon points="0,252 658,127 658,170 0,295" fill="url(#bandShade)"/>
      <polygon points="0,137 658,14 658,127 0,252" fill="url(#bandFill)"/>
      <path d="M172,202 C186,212 196,232 200,262 C230,212 290,176 357,164 C300,170 240,200 199,297 C196,258 186,224 172,202 Z" fill="var(--tick-red)"/>
    </svg>

    <div class="brand">
      <div class="brand__mark"></div>
      <div class="brand__name">Halden</div>
    </div>

    <h1 class="headline">Do you have developer clients?</h1>

    <p class="pitch">We can help with Lot Entitlements for Land Division. We believe that our prices are the best in the market, however should you provide a cheaper written quote we will beat it by <span class="pitch__figure">15%.</span></p>

    <div class="pricing">
      <p class="pricing__title">Pricing for RVB compliant Lot Entitlement Certificates.</p>
      <ul class="pricing__list">
        <li class="pricing__item">1 Allotment into 2 Community Titled Lots: $220 Inc GST <span>(2 day turnaround)</span></li>
        <li class="pricing__item">1 Allotment into 3 Community Titled Lots: $275 Inc GST <span>(2 day turnaround)</span></li>
        <li class="pricing__item">1 Allotment into 4 or 5 Community Titled Lots: $330 Inc GST <span>(2 day turnaround)</span></li>
        <li class="pricing__item">6 or more or Commercial: By Quote</li>
      </ul>
    </div>
  </section>
</body>
</html>
```